Business Card Design Project

Business card design with a funky, clean, modern design. Business is an immigration consultancy. Client base will be Canadian employers wanting to hire or retain foreign workers and foreign nationals wanting to immigrate to Canada.

Full color possible, but should incorporate red/white/black as per the logo to be provided. Double sided card design.

Target Market(s)

Canadian employers looking to hire/retain staff and also foreign nationals immigrating to Canada

Industry/Entity Type

Business

Requirements
Must have
• Logo (to be provided)
Name (Marla Quintero, Immigration Consultant)
Phone (604) 517-3362
E-mail: marla@lanternpathvisas.example
Web: www.lanternpathvisas.example

Nice to have
• Tag Line
Clean, modern style

```html
<!DOCTYPE html>
<html lang="en">
<head>
<meta charset="utf-8">
<title>Lantern Path Visas – Business Card Print Sheet</title>
<link href="https://fonts.googleapis.com/css2?family=Open+Sans:wght@400;700;800&display=swap" rel="stylesheet">
<style>
  :root {
    --paper: #ffffff;
    --ink: #111111;
    --card: #000000;
    --brand-red: #c8102e;
    --label-red: #b5123a;
    --text-light: #e6e6e6;
    --text-muted: #9a9a9a;
    --cut-line: #555555;
  }
  * { margin: 0; padding: 0; box-sizing: border-box; }
  html, body { width: 915px; height: 1200px; overflow: hidden; background: var(--paper); }
  body { font-family: "Open Sans", Arial, sans-serif; position: relative; }

  .sheet { position: relative; width: 915px; height: 1200px; }

  .side-label {
    position: absolute; width: 383px; text-align: center;
    font-weight: 800; font-size: 36px; color: var(--ink); line-height: 1;
  }
  .side-label.front { left: 51px; }
  .side-label.back { left: 499px; }
  .side-label.top { top: 8px; }
  .side-label.bottom { top: 1112px; }

  .cut-line { position: absolute; border: 0 dashed var(--cut-line); }
  .cut-line.horizontal { left: 0; width: 915px; border-top-width: 1.5px; }
  .cut-line.vertical { top: 0; height: 1200px; border-left-width: 1.5px; }

  .card {
    position: absolute; width: 383px; height: 218px; background: var(--card);
  }
  .card.front { left: 51px; }
  .card.back { left: 499px; }

  .front .brand-mark {
    position: absolute; left: 262px; top: 44px;
    font-weight: 800; font-size: 17px; color: var(--brand-red);
    line-height: 1.1; letter-spacing: 0.5px;
  }
  .front .holder-name {
    position: absolute; left: 21px; top: 102px;
    font-weight: 700; font-size: 12.5px; color: var(--label-red);
  }
  .front .holder-title {
    position: absolute; left: 51px; top: 122px;
    font-size: 10px; color: var(--text-muted);
  }
  .front .contact {
    position: absolute; left: 21px; top: 168px;
    font-size: 10.5px; color: var(--text-light); line-height: 18px;
  }
  .front .contact .field { font-weight: 700; font-size: 12.5px; color: var(--label-red); margin-right: 3px; }

  .back .brand-dot {
    position: absolute; left: 161px; top: 38px; width: 62px; height: 62px;
    border-radius: 50%; background: var(--brand-red);
  }
  .back .brand-name {
    position: absolute; left: 0; width: 383px; top: 118px; text-align: center;
    font-weight: 800; font-size: 24px; color: #ffffff; letter-spacing: 0.5px;
  }
  .back .web {
    position: absolute; left: 0; width: 383px; top: 200px; text-align: center;
    font-size: 7px; color: var(--brand-red);
  }
</style>
</head>
<body>
<main class="sheet">
  <div class="side-label front top">Front</div>
  <div class="side-label back top">Back</div>

  <div class="cut-line vertical" style="left:439px"></div>
  <div class="cut-line vertical" style="left:492px"></div>
  <div class="cut-line horizontal" style="top:268px"></div>
  <div class="cut-line horizontal" style="top:310px"></div>
  <div class="cut-line horizontal" style="top:537px"></div>
  <div class="cut-line horizontal" style="top:579px"></div>
  <div class="cut-line horizontal" style="top:806px"></div>
  <div class="cut-line horizontal" style="top:849px"></div>

  <!-- Row 1 -->
  <section class="card front" style="top:47px">
    <div class="brand-mark">LANTERN<br>PATH</div>
    <div class="holder-name">Marla Quintero</div>
    <div class="holder-title">RCIC</div>
    <div class="contact">
      <div><span class="field">Phone</span>(604) 517-3362</div>
      <div><span class="field">E-mail</span>marla@lanternpathvisas.example</div>
    </div>
  </section>
  <section class="card back" style="top:47px">
    <div class="brand-dot"></div>
    <div class="brand-name">LANTERN PATH VISAS</div>
    <div class="web">www.lanternpathvisas.example</div>
  </section>

  <!-- Row 2 -->
  <section class="card front" style="top:316px">
    <div class="brand-mark">LANTERN<br>PATH</div>
    <div class="holder-name">Marla Quintero</div>
    <div class="holder-title">RCIC</div>
    <div class="contact">
      <div><span class="field">Phone</span>(604) 517-3362</div>
      <div><span class="field">E-mail</span>marla@lanternpathvisas.example</div>
    </div>
  </section>
  <section class="card back" style="top:316px">
    <div class="brand-dot"></div>
    <div class="brand-name">LANTERN PATH VISAS</div>
    <div class="web">www.lanternpathvisas.example</div>
  </section>

  <!-- Row 3 -->
  <section class="card front" style="top:585px">
    <div class="brand-mark">LANTERN<br>PATH</div>
    <div class="holder-name">Marla Quintero</div>
    <div class="holder-title">RCIC</div>
    <div class="contact">
      <div><span class="field">Phone</span>(604) 517-3362</div>
      <div><span class="field">E-mail</span>marla@lanternpathvisas.example</div>
    </div>
  </section>
  <section class="card back" style="top:585px">
    <div class="brand-dot"></div>
    <div class="brand-name">LANTERN PATH VISAS</div>
    <div class="web">www.lanternpathvisas.example</div>
  </section>

  <!-- Row 4 -->
  <section class="card front" style="top:855px">
    <div class="brand-mark">LANTERN<br>PATH</div>
    <div class="holder-name">Marla Quintero</div>
    <div class="holder-title">RCIC</div>
    <div class="contact">
      <div><span class="field">Phone</span>(604) 517-3362</div>
      <div><span class="field">E-mail</span>marla@lanternpathvisas.example</div>
    </div>
  </section>
  <section class="card back" style="top:855px">
    <div class="brand-dot"></div>
    <div class="brand-name">LANTERN PATH VISAS</div>
    <div class="web">www.lanternpathvisas.example</div>
  </section>

  <div class="side-label front bottom">Front</div>
  <div class="side-label back bottom">Back</div>
</main>
</body>
</html>
```